Volunteer fire fighters needed banner

As part of our recruitment campaign, we need a sign we can post on our sign trailer to entice locals to join our volunteer fire service. This design will be printed on a banner, front and back, to catch traffic going in both directions on a busy roadway. This banner will have a printed surface of 4 feet tall by 8 feet long.
Our fire department is looking to attract people between the ages of 18 and 35 years old who are interested in being a firefighter. We offer our volunteers:
-Free professional training
-All equipment supplied
-Tax abatements for active volunteers
For more information, you can check us out at:
Brookmerecrestfire.example

This design should:
-scale to and fit a 4'x8' canvas
-Include our web address "BrookmereCrestFire.example"
-Say "Members Wanted"
-"Drill every Tuesday at 7pm"
-"37 Quarry Bend Lane"
-Include "Brookmere Crest Fire Department"

We've included reference photos and past images we use for our other campaigns for inspiration for you.

Target Market(s)

18-35 y/o

Industry/Entity Type

Fire Service

Requirements
Must have
• -scale to and fit a 4'x8' canvas -Include our web address "BrookmereCrestFire.example" -Say "Members Wanted" -"Drill every Tuesday at 7pm" -"37 Quarry Bend Lane" -Include "Brookmere Crest Fire Department"

```html
<!DOCTYPE html>
<html lang="en">
<head>
<meta charset="utf-8">
<title>Members Wanted – Brookmere Crest Fire Department</title>
<link href="https://fonts.googleapis.com/css2?family=Anton&family=Montserrat:wght@600;700&family=Roboto+Condensed:wght@500&display=swap" rel="stylesheet">
<style>
  :root {
    --navy: #2a3585;
    --royal: #3a47a8;
    --red: #e0222e;
    --white: #ffffff;
    --paper: #eeeeee;
    --ink: #4a4a4a;
    --stage: #e4e6ea;
  }
  html, body {
    margin: 0;
    width: 1054px;
    height: 1200px;
    overflow: hidden;
    background: var(--stage);
  }
  .banner {
    position: absolute;
    left: 27px;
    top: 350px;
    width: 1000px;
    height: 500px;
    overflow: hidden;
    background: radial-gradient(ellipse at 40% 30%, #ffffff 0%, var(--paper) 70%, #dcdcdc 100%);
  }
  .banner__shapes {
    position: absolute;
    inset: 0;
  }
  .headline {
    position: absolute;
    left: 30px;
    top: 16px;
    margin: 0;
    font-family: "Anton", sans-serif;
    font-weight: 400;
    font-size: 100px;
    line-height: 100px;
    letter-spacing: 1px;
  }
  .headline__top { display: block; color: var(--navy); }
  .headline__bottom { display: block; color: var(--red); }
  .drill-band {
    position: absolute;
    left: 0;
    top: 228px;
    width: 510px;
    height: 40px;
    background: var(--royal);
    color: var(--white);
    font-family: "Roboto Condensed", sans-serif;
    font-weight: 500;
    font-size: 34px;
    line-height: 40px;
    padding-left: 26px;
    box-sizing: border-box;
  }
  .benefits {
    position: absolute;
    left: 14px;
    top: 288px;
    display: flex;
    list-style: none;
    margin: 0;
    padding: 0;
  }
  .benefit {
    width: 136px;
    text-align: center;
    font-family: "Montserrat", sans-serif;
    font-weight: 600;
    font-size: 9.5px;
    line-height: 12px;
    color: var(--ink);
    letter-spacing: .5px;
  }
  .benefit svg { display: block; margin: 0 auto 10px; }
  .contact {
    position: absolute;
    left: 0;
    font-family: "Montserrat", sans-serif;
    font-weight: 700;
    color: var(--white);
    display: flex;
    align-items: center;
    gap: 10px;
    padding-left: 26px;
    box-sizing: border-box;
    white-space: nowrap;
  }
  .contact--address {
    top: 418px;
    height: 38px;
    width: 430px;
    background: var(--royal);
    clip-path: polygon(0 0, 96% 0, 100% 100%, 0 100%);
    font-size: 24px;
    letter-spacing: 1.5px;
  }
  .contact--web {
    top: 458px;
    height: 42px;
    width: 500px;
    background: var(--red);
    clip-path: polygon(0 0, 96% 0, 100% 100%, 0 100%);
    font-size: 24px;
  }
  .truck-photo {
    position: absolute;
    left: 505px;
    top: 50px;
    width: 480px;
    height: 390px;
    border-radius: 30px;
    background: radial-gradient(ellipse at 45% 55%, #e8333f 0%, #c5202b 40%, #6b3a6a 75%, rgba(58,71,168,0) 100%);
  }
  .dept-mark {
    position: absolute;
    right: 16px;
    bottom: 14px;
    display: flex;
    align-items: center;
    gap: 7px;
    font-family: "Montserrat", sans-serif;
    font-weight: 700;
    font-size: 11px;
    line-height: 13px;
    color: var(--white);
  }
  .dept-mark__dot {
    flex: none;
    width: 16px;
    height: 16px;
    border-radius: 50%;
    background: var(--red);
  }
</style>
</head>
<body>
  <section class="banner" aria-label="Volunteer firefighter recruitment banner">
    <svg class="banner__shapes" width="1000" height="500" viewBox="0 0 1000 500" aria-hidden="true">
      <defs>
        <linearGradient id="panelBlue" x1="0" y1="0" x2="1" y2="1">
          <stop offset="0" stop-color="#3d4bb0"/>
          <stop offset="1" stop-color="#27318a"/>
        </linearGradient>
      </defs>
      <polygon points="584,0 1000,0 1000,500 606,500 530,200" fill="url(#panelBlue)"/>
      <polygon points="562,0 584,0 530,200 606,500 586,500 510,200" fill="var(--red)"/>
    </svg>

    <h1 class="headline">
      <span class="headline__top">MEMBERS</span>
      <span class="headline__bottom">WANTED</span>
    </h1>

    <div class="drill-band">DRILL EVERY TUESDAY AT 7PM</div>

    <ul class="benefits">
      <li class="benefit">
        <svg width="70" height="62" viewBox="0 0 62 54">
          <circle cx="31" cy="27" r="25" fill="none" stroke="var(--red)" stroke-width="2"/>
          <circle cx="31" cy="18" r="5" fill="var(--red)"/>
          <path d="M22 34c0-6 4-9 9-9s9 3 9 9z" fill="var(--red)"/>
          <rect x="19" y="34" width="24" height="3" fill="var(--red)"/>
        </svg>
        FREE PROFESSIONAL TRAINING
      </li>
      <li class="benefit">
        <svg width="70" height="62" viewBox="0 0 62 54">
          <circle cx="31" cy="27" r="25" fill="none" stroke="var(--red)" stroke-width="2"/>
          <circle cx="29" cy="25" r="9" fill="none" stroke="var(--red)" stroke-width="5" stroke-dasharray="4 3"/>
          <circle cx="29" cy="25" r="6" fill="none" stroke="var(--red)" stroke-width="2"/>
          <line x1="31" y1="27" x2="42" y2="38" stroke="var(--red)" stroke-width="4" stroke-linecap="round"/>
        </svg>
        ALL EQUIPMENT SUPPLIED
      </li>
      <li class="benefit">
        <svg width="70" height="62" viewBox="0 0 62 54">
          <circle cx="31" cy="27" r="25" fill="none" stroke="var(--red)" stroke-width="2"/>
          <path d="M27 14h8l-2 4c6 3 9 9 9 15 0 3-2 5-5 5H25c-3 0-5-2-5-5 0-6 3-12 9-15z" fill="var(--red)"/>
          <text x="31" y="33" text-anchor="middle" font-family="Montserrat, sans-serif" font-size="11" font-weight="700" fill="#fff">$%</text>
        </svg>
        TAX ABATEMENTS FOR ACTIVE VOLUNTEERS
      </li>
    </ul>

    <div class="contact contact--address">
      <svg width="18" height="21" viewBox="0 0 18 20" aria-hidden="true">
        <path d="M9 1a7 7 0 0 0-7 7c0 5 7 11 7 11s7-6 7-11a7 7 0 0 0-7-7z" fill="none" stroke="#fff" stroke-width="2"/>
        <circle cx="9" cy="8" r="2.5" fill="#fff"/>
      </svg>
      37 QUARRY BEND LANE
    </div>
    <div class="contact contact--web">
      <svg width="21" height="21" viewBox="0 0 20 20" aria-hidden="true">
        <circle cx="10" cy="10" r="8.5" fill="none" stroke="#fff" stroke-width="1.8"/>
        <ellipse cx="10" cy="10" rx="3.5" ry="8.5" fill="none" stroke="#fff" stroke-width="1.5"/>
        <line x1="1.5" y1="10" x2="18.5" y2="10" stroke="#fff" stroke-width="1.5"/>
      </svg>
      BrookmereCrestFire.example
    </div>

    <div class="truck-photo" role="img" aria-label="Photo of a red fire department tanker truck"></div>

    <div class="dept-mark">
      <span class="dept-mark__dot"></span>
      <span>Brookmere Crest<br>Fire Department</span>
    </div>
  </section>
</body>
</html>
```